Increased budget: GUI redesign: 10 year old user interface needs modern look-and-feel

UPDATE: Please DO look at more than only th eone image I attached! Almost all designs are simply reworks of that one picture. That is not what we are looking for. Check out the video to understand what the product does, and try to make something better.
We have an existing app (see https://www.vornatek.com/downloadTunePilot.php?vers=3_9_1_140964&dir=Vornatek_OEM/3_9_1_140964&name=DSP_Control_Software) which needs refreshing. See also a video here: https://vornatek-oem.com/software/ and the user manual attached here. The GUI is now 800x400 pixels, which is too small; and not scalable, which will be fixed in the future. We need a new, modern look-and-feel, and images that can be exported from the design in various sizes. The current design is attached as well as a collection of PNG files. The overall layout can stay similar, although we are open to good ideas for improvements. The design should be targeted at professional users, not end users; the product is used by audio professionals (e.g. sound engineers, loudspeaker designers). Also see our web version: https://www.vornatek.com/tunepilot/skins/1_1_2/container.html?MAC=Demo%201x2
The winner will also be asked to do a full design of the application GUI (based on the design done here), with several more windows etc, and additional payment depending on the work to be done.

Target Market(s)

Professional audio

Industry/Entity Type

Audio / Industrial

Font styles to use
Other font styles liked:
• Futura (not mandatory)

Colors

Designer to choose colors to be used in the design.

Requirements
Must have
• Modern, timeless design, not too bling bling
Nice to have
• Flat design
Should not have
• 3D, bling bling, many colours, etc

```html
<!DOCTYPE html>
<html lang="en">
<head>
<meta charset="utf-8">
<title>Vornatek TunePilot – Output EQ</title>
<link href="https://fonts.googleapis.com/css2?family=Outfit:wght@400;500;600&display=swap" rel="stylesheet">
<style>
:root{
  --bg:#717a92;
  --panel:#dddddd;
  --field:#d3d3d3;
  --field-edge:#c4c4c4;
  --ink:#111111;
  --screen:#0a0a0a;
  --grid:#3a3a3a;
  --curve:#f57c00;
  --brand:#0d2a3c;
  --teal:#5fe8c8;
}
*{box-sizing:border-box;margin:0;padding:0}
html,body{width:1200px;height:674px;overflow:hidden;background:var(--bg);font-family:"Outfit",sans-serif;color:var(--ink)}
.stage{position:absolute;left:0;top:0;width:2576px;height:1447px;transform:scale(.46584);transform-origin:0 0}
.panel{position:absolute;background:var(--panel);border-radius:26px}
.abs{position:absolute}

.sidebar{left:20px;top:22px;width:323px;height:1406px}
.brand{position:absolute;left:62px;top:150px;display:flex;align-items:center;gap:14px}
.brand-mark{width:34px;height:34px;background:var(--brand)}
.brand-name{font-size:34px;font-weight:600;color:var(--brand);letter-spacing:1px}
.nav-btn{position:absolute;left:23px;width:275px;height:98px;border:2px solid #c8c8c8;border-radius:10px;background:#d8d8d8;
  display:flex;align-items:center;justify-content:center;font-size:30px;font-weight:600;box-shadow:0 3px 4px rgba(0,0,0,.08)}

.graph-panel{left:357px;top:22px;width:1840px;height:748px}
.graph{position:absolute;left:382px;top:44px;width:1792px;height:704px;border-radius:18px;background:var(--screen);overflow:hidden}

.meter-panel{left:2215px;top:22px;width:340px;height:748px}

.eq-panel{left:357px;top:788px;width:1355px;height:640px}
.col-head{position:absolute;top:818px;font-size:32px;font-weight:500;transform:translateX(-50%)}
.field{position:absolute;height:62px;background:var(--field);border-radius:8px;box-shadow:0 2px 3px rgba(0,0,0,.12);
  display:flex;align-items:center;font-size:23px;font-weight:500}
.field.center{justify-content:center}
.field.pad{padding-left:24px}
.field .chev{position:absolute;right:24px;top:22px}
.on-btn{position:absolute;width:61px;height:62px;background:var(--field);border-radius:8px;box-shadow:0 2px 3px rgba(0,0,0,.12);display:flex;align-items:center;justify-content:center}
.on-btn.active{border:2px solid #222}
.filter-label{position:absolute;top:1250px;font-size:28px;font-weight:600}

.dyn-panel{left:1729px;top:788px;width:826px;height:640px}
.mute-label{position:absolute;left:2343px;top:812px;font-size:30px;font-weight:500}
.toggle{position:absolute;left:2430px;top:806px;width:100px;height:52px;border-radius:6px;background:#3f4552}
.toggle-knob{position:absolute;right:6px;top:6px;width:50px;height:40px;border-radius:5px;background:#f4f4f4;display:flex;align-items:center;justify-content:center;gap:4px}
.toggle-knob i{width:2px;height:14px;background:#777}
.dyn-title{position:absolute;top:928px;font-size:33px;font-weight:500;transform:translateX(-50%)}
.dyn-rule{position:absolute;top:980px;width:46px;height:3px;background:#b8b8b8;transform:translateX(-50%)}
.dyn-value{position:absolute;top:1252px;width:166px;height:64px;background:var(--field);border-radius:8px;box-shadow:0 2px 3px rgba(0,0,0,.12);
  display:flex;align-items:center;justify-content:center;font-size:24px;font-weight:500;transform:translateX(-50%)}
.dyn-unit{position:absolute;top:1332px;font-size:33px;font-weight:600;transform:translateX(-50%)}
</style>
</head>
<body>
<div class="stage">

  <!-- Sidebar -->
  <aside class="panel sidebar">
    <div class="brand"><span class="brand-mark"></span><span class="brand-name">VORNATEK</span></div>
  </aside>
  <div class="nav-btn" style="top:306px">MAIN</div>
  <div class="nav-btn" style="top:416px">X-OVER</div>
  <div class="nav-btn" style="top:527px">IN 1</div>
  <div class="nav-btn" style="top:637px">IN 2</div>
  <div class="nav-btn" style="top:747px">IN 3</div>
  <div class="nav-btn" style="top:857px">OUT 1</div>
  <div class="nav-btn" style="top:967px">OUT 2</div>
  <div class="nav-btn" style="top:1078px">OUT 3</div>
  <div class="nav-btn" style="top:1189px">OUT 4</div>

  <!-- EQ graph -->
  <section class="panel graph-panel"></section>
  <div class="graph">
    <svg width="1792" height="704" viewBox="0 0 1792 704">
      <g stroke="var(--grid)" stroke-width="2">
        <line x1="0" y1="182" x2="1792" y2="182"/><line x1="0" y1="504" x2="1792" y2="504"/>
        <line x1="198" y1="0" x2="198" y2="704"/><line x1="293" y1="0" x2="293" y2="704"/><line x1="361" y1="0" x2="361" y2="704"/>
        <line x1="413" y1="0" x2="413" y2="704"/><line x1="454" y1="0" x2="454" y2="704"/><line x1="489" y1="0" x2="489" y2="704"/>
        <line x1="521" y1="0" x2="521" y2="704"/><line x1="549" y1="0" x2="549" y2="704"/><line x1="575" y1="0" x2="575" y2="704"/>
        <line x1="733" y1="0" x2="733" y2="704"/><line x1="828" y1="0" x2="828" y2="704"/><line x1="896" y1="0" x2="896" y2="704"/>
        <line x1="948" y1="0" x2="948" y2="704"/><line x1="989" y1="0" x2="989" y2="704"/><line x1="1024" y1="0" x2="1024" y2="704"/>
        <line x1="1055" y1="0" x2="1055" y2="704"/><line x1="1083" y1="0" x2="1083" y2="704"/><line x1="1110" y1="0" x2="1110" y2="704"/>
        <line x1="1268" y1="0" x2="1268" y2="704"/><line x1="1363" y1="0" x2="1363" y2="704"/><line x1="1431" y1="0" x2="1431" y2="704"/>
        <line x1="1483" y1="0" x2="1483" y2="704"/><line x1="1524" y1="0" x2="1524" y2="704"/><line x1="1559" y1="0" x2="1559" y2="704"/>
        <line x1="1590" y1="0" x2="1590" y2="704"/><line x1="1618" y1="0" x2="1618" y2="704"/><line x1="1645" y1="0" x2="1645" y2="704"/>
      </g>
      <line x1="0" y1="352" x2="1792" y2="352" stroke="var(--curve)" stroke-width="4"/>
      <g font-family="Outfit,sans-serif" font-size="19" font-weight="600" text-anchor="middle">
        <circle cx="234" cy="352" r="24" fill="#f57c00"/><text x="234" y="359">1</text>
        <circle cx="390" cy="352" r="24" fill="#aaa3da"/><text x="390" y="359">2</text>
        <circle cx="574" cy="352" r="24" fill="#e8101a"/><text x="574" y="359">3</text>
        <circle cx="733" cy="352" r="24" fill="#f57c00"/><text x="733" y="359">4</text>
        <circle cx="895" cy="352" r="24" fill="#a6e21a"/><text x="895" y="359">5</text>
        <circle cx="1060" cy="352" r="24" fill="#d9344e"/><text x="1060" y="359">6</text>
        <circle cx="1269" cy="352" r="24" fill="#b520c9"/><text x="1269" y="359">7</text>
        <circle cx="1431" cy="352" r="24" fill="#e2ccb4"/><text x="1431" y="359">8</text>
        <circle cx="1560" cy="352" r="24" fill="#c2406c"/><text x="1560" y="359">9</text>
        <circle cx="1699" cy="352" r="24" fill="#f57c00"/><text x="1699" y="359">10</text>
      </g>
    </svg>
  </div>

  <!-- Level meter / fader -->
  <section class="panel meter-panel"></section>
  <svg class="abs" style="left:2215px;top:22px" width="340" height="748" viewBox="2215 22 340 748">
    <defs>
      <pattern id="ticks" width="6" height="5.95" patternUnits="userSpaceOnUse" x="0" y="74">
        <rect width="6" height="1.6" fill="#555"/>
      </pattern>
      <linearGradient id="level" x1="0" y1="0" x2="0" y2="1">
        <stop offset="0" stop-color="#5fa892"/><stop offset="1" stop-color="var(--teal)"/>
      </linearGradient>
    </defs>
    <g font-family="Outfit,sans-serif" font-size="19" fill="#222" text-anchor="middle">
      <text x="2268" y="80">+12</text><text x="2268" y="139">+6</text><text x="2268" y="199">0</text>
      <text x="2268" y="258">-6</text><text x="2268" y="318">-12</text><text x="2268" y="377">-18</text>
      <text x="2268" y="437">-24</text><text x="2268" y="496">-30</text><text x="2268" y="556">-36</text>
      <text x="2268" y="615">-42</text><text x="2268" y="675">-48</text>
      <text x="2485" y="81">+12</text><text x="2485" y="141">+6</text><text x="2485" y="200">0</text>
      <text x="2485" y="260">-6</text><text x="2485" y="319">-12</text><text x="2485" y="379">-18</text>
      <text x="2485" y="438">-24</text><text x="2485" y="498">-30</text><text x="2485" y="557">-36</text>
      <text x="2485" y="617">-42</text><text x="2485" y="676">-48</text>
    </g>
    <rect x="2320" y="74" width="12" height="594" fill="url(#ticks)"/>
    <rect x="2424" y="74" width="12" height="594" fill="url(#ticks)"/>
    <g stroke="#555" stroke-width="2">
      <line x1="2305" y1="74" x2="2332" y2="74"/><line x1="2305" y1="133" x2="2332" y2="133"/><line x1="2305" y1="193" x2="2332" y2="193"/>
      <line x1="2305" y1="252" x2="2332" y2="252"/><line x1="2305" y1="312" x2="2332" y2="312"/><line x1="2305" y1="371" x2="2332" y2="371"/>
      <line x1="2305" y1="431" x2="2332" y2="431"/><line x1="2305" y1="490" x2="2332" y2="490"/><line x1="2305" y1="550" x2="2332" y2="550"/>
      <line x1="2305" y1="609" x2="2332" y2="609"/><line x1="2305" y1="668" x2="2332" y2="668"/>
      <line x1="2424" y1="74" x2="2450" y2="74"/><line x1="2424" y1="133" x2="2450" y2="133"/><line x1="2424" y1="193" x2="2450" y2="193"/>
      <line x1="2424" y1="252" x2="2450" y2="252"/><line x1="2424" y1="312" x2="2450" y2="312"/><line x1="2424" y1="371" x2="2450" y2="371"/>
      <line x1="2424" y1="431" x2="2450" y2="431"/><line x1="2424" y1="490" x2="2450" y2="490"/><line x1="2424" y1="550" x2="2450" y2="550"/>
      <line x1="2424" y1="609" x2="2450" y2="609"/><line x1="2424" y1="668" x2="2450" y2="668"/>
    </g>
    <rect x="2368" y="74" width="20" height="596" rx="10" fill="#e9e9e9"/>
    <rect x="2368" y="360" width="20" height="310" rx="10" fill="url(#level)"/>
    <rect x="2348" y="300" width="58" height="78" rx="6" fill="#e2e2e2" stroke="#c9c9c9" stroke-width="2"/>
    <g stroke="#6a7080" stroke-width="3"><line x1="2368" y1="330" x2="2386" y2="330"/><line x1="2368" y1="339" x2="2386" y2="339"/><line x1="2368" y1="348" x2="2386" y2="348"/></g>
    <text x="2381" y="738" font-family="Outfit,sans-serif" font-size="24" text-anchor="middle" fill="#111">0.00 dB</text>
  </svg>

  <!-- Parametric EQ table -->
  <section class="panel eq-panel"></section>
  <div class="col-head" style="left:426px">ON</div>
  <div class="col-head" style="left:520px">Type</div>
  <div class="col-head" style="left:720px">Freq</div>
  <div class="col-head" style="left:866px">Q</div>
  <div class="col-head" style="left:958px">Gain</div>
  <div class="col-head" style="left:1093px">ON</div>
  <div class="col-head" style="left:1188px">Type</div>
  <div class="col-head" style="left:1387px">Freq</div>
  <div class="col-head" style="left:1533px">Q</div>
  <div class="col-head" style="left:1626px">Gain</div>

  <svg width="0" height="0" style="position:absolute">
    <defs>
      <symbol id="wave" viewBox="0 0 34 34">
        <g stroke="#333" stroke-width="1.6">
          <line x1="2" y1="15" x2="2" y2="19"/><line x1="5" y1="12" x2="5" y2="22"/><line x1="8" y1="14" x2="8" y2="20"/>
          <line x1="11" y1="6" x2="11" y2="28"/><line x1="14" y1="3" x2="14" y2="31"/><line x1="17" y1="8" x2="17" y2="26"/>
          <line x1="20" y1="11" x2="20" y2="23"/><line x1="23" y1="13" x2="23" y2="21"/><line x1="26" y1="15" x2="26" y2="19"/>
          <line x1="29" y1="16" x2="29" y2="18"/><line x1="32" y1="16" x2="32" y2="18"/>
        </g>
      </symbol>
      <symbol id="chev" viewBox="0 0 16 10"><path d="M1 1l7 7 7-7" fill="none" stroke="#222" stroke-width="2"/></symbol>
    </defs>
  </svg>

  <!-- left bank rows -->
  <div class="on-btn active" style="left:398px;top:875px"><svg width="34" height="34"><use href="#wave"/></svg></div>
  <div class="on-btn active" style="left:398px;top:945px"><svg width="34" height="34"><use href="#wave"/></svg></div>
  <div class="on-btn" style="left:398px;top:1015px"></div>
  <div class="on-btn" style="left:398px;top:1085px"></div>
  <div class="on-btn" style="left:398px;top:1155px"></div>

  <div class="field pad" style="left:469px;top:875px;width:201px">Bell<svg class="chev" width="16" height="10"><use href="#chev"/></svg></div>
  <div class="field pad" style="left:469px;top:945px;width:201px">Bell<svg class="chev" width="16" height="10"><use href="#chev"/></svg></div>
  <div class="field pad" style="left:469px;top:1015px;width:201px">Bell<svg class="chev" width="16" height="10"><use href="#chev"/></svg></div>
  <div class="field pad" style="left:469px;top:1085px;width:201px">Bell<svg class="chev" width="16" height="10"><use href="#chev"/></svg></div>
  <div class="field pad" style="left:469px;top:1155px;width:201px">Bell<svg class="chev" width="16" height="10"><use href="#chev"/></svg></div>

  <div class="field pad" style="left:681px;top:875px;width:145px;padding-left:16px">20Hz</div>
  <div class="field pad" style="left:681px;top:945px;width:145px;padding-left:16px">20Hz</div>
  <div class="field pad" style="left:681px;top:1015px;width:145px;padding-left:16px">20Hz</div>
  <div class="field pad" style="left:681px;top:1085px;width:145px;padding-left:16px">20Hz</div>
  <div class="field pad" style="left:681px;top:1155px;width:145px;padding-left:16px">20Hz</div>

  <div class="field center" style="left:836px;top:875px;width:61px">1</div>
  <div class="field center" style="left:836px;top:945px;width:61px">1</div>
  <div class="field center" style="left:836px;top:1015px;width:61px">1</div>
  <div class="field center" style="left:836px;top:1085px;width:61px">1</div>
  <div class="field center" style="left:836px;top:1155px;width:61px">1</div>

  <div class="field center" style="left:908px;top:875px;width:103px">0db</div>
  <div class="field center" style="left:908px;top:945px;width:103px">0db</div>
  <div class="field center" style="left:908px;top:1015px;width:103px">0db</div>
  <div class="field center" style="left:908px;top:1085px;width:103px">0db</div>
  <div class="field center" style="left:908px;top:1155px;width:103px">0db</div>

  <!-- right bank rows -->
  <div class="on-btn" style="left:1065px;top:875px"></div>
  <div class="on-btn active" style="left:1065px;top:945px"><svg width="34" height="34"><use href="#wave"/></svg></div>
  <div class="on-btn active" style="left:1065px;top:1015px"><svg width="34" height="34"><use href="#wave"/></svg></div>
  <div class="on-btn" style="left:1065px;top:1085px"></div>
  <div class="on-btn" style="left:1065px;top:1155px"></div>

  <div class="field pad" style="left:1136px;top:875px;width:202px">Bell<svg class="chev" width="16" height="10"><use href="#chev"/></svg></div>
  <div class="field pad" style="left:1136px;top:945px;width:202px">Bell<svg class="chev" width="16" height="10"><use href="#chev"/></svg></div>
  <div class="field pad" style="left:1136px;top:1015px;width:202px">Bell<svg class="chev" width="16" height="10"><use href="#chev"/></svg></div>
  <div class="field pad" style="left:1136px;top:1085px;width:202px">Bell<svg class="chev" width="16" height="10"><use href="#chev"/></svg></div>
  <div class="field pad" style="left:1136px;top:1155px;width:202px">Bell<svg class="chev" width="16" height="10"><use href="#chev"/></svg></div>

  <div class="field pad" style="left:1348px;top:875px;width:145px;padding-left:16px">20Hz</div>
  <div class="field pad" style="left:1348px;top:945px;width:145px;padding-left:16px">20Hz</div>
  <div class="field pad" style="left:1348px;top:1015px;width:145px;padding-left:16px">20Hz</div>
  <div class="field pad" style="left:1348px;top:1085px;width:145px;padding-left:16px">20Hz</div>
  <div class="field pad" style="left:1348px;top:1155px;width:145px;padding-left:16px">20Hz</div>

  <div class="field center" style="left:1503px;top:875px;width:62px">1</div>
  <div class="field center" style="left:1503px;top:945px;width:62px">1</div>
  <div class="field center" style="left:1503px;top:1015px;width:62px">1</div>
  <div class="field center" style="left:1503px;top:1085px;width:62px">1</div>
  <div class="field center" style="left:1503px;top:1155px;width:62px">1</div>

  <div class="field center" style="left:1575px;top:875px;width:103px">0db</div>
  <div class="field center" style="left:1575px;top:945px;width:103px">0db</div>
  <div class="field center" style="left:1575px;top:1015px;width:103px">0db</div>
  <div class="field center" style="left:1575px;top:1085px;width:103px">0db</div>
  <div class="field center" style="left:1575px;top:1155px;width:103px">0db</div>

  <!-- HPF / LPF -->
  <div class="filter-label" style="left:447px">HPF</div>
  <div class="field pad" style="left:435px;top:1292px;width:202px;height:60px;padding-left:26px">Off</div>
  <div class="field pad" style="left:645px;top:1292px;width:333px;height:60px;padding-left:36px">Butterworth&nbsp; 6dB<svg class="chev" width="16" height="10" style="top:25px"><use href="#chev"/></svg></div>
  <div class="filter-label" style="left:1118px">LPF</div>
  <div class="field pad" style="left:1106px;top:1292px;width:201px;height:60px;padding-left:20px">Off</div>
  <div class="field pad" style="left:1316px;top:1292px;width:332px;height:60px;padding-left:44px">Butterworth 6dB<svg class="chev" width="16" height="10" style="top:25px"><use href="#chev"/></svg></div>

  <!-- Dynamics -->
  <section class="panel dyn-panel"></section>
  <div class="mute-label">Mute</div>
  <div class="toggle"><div class="toggle-knob"><i></i><i></i><i></i></div></div>

  <div class="dyn-title" style="left:1898px">Delay</div>
  <div class="dyn-title" style="left:2142px">Limiter</div>
  <div class="dyn-title" style="left:2378px">Compressor</div>
  <div class="dyn-rule" style="left:1898px"></div>
  <div class="dyn-rule" style="left:2142px"></div>
  <div class="dyn-rule" style="left:2380px"></div>

  <svg class="abs" style="left:1780px;top:1000px" width="740" height="220" viewBox="1780 1000 740 220">
    <defs>
      <radialGradient id="knobFace" cx=".4" cy=".35" r=".8">
        <stop offset="0" stop-color="#b4b4b4"/><stop offset="1" stop-color="#8e8e8e"/>
      </radialGradient>
    </defs>
    <g fill="none" stroke="#333" stroke-width="3" stroke-dasharray="1.5 10" stroke-linecap="round">
      <path d="M1843 1177 A90 90 0 1 1 1971 1177"/>
      <path d="M2078 1177 A90 90 0 1 1 2206 1177"/>
      <path d="M2314 1177 A90 90 0 1 1 2442 1177"/>
    </g>
    <g stroke="#2a2a2a" stroke-width="2" fill="url(#knobFace)">
      <circle cx="1907" cy="1112" r="67"/>
      <circle cx="2142" cy="1112" r="67"/>
      <circle cx="2378" cy="1112" r="67"/>
    </g>
    <g fill="#2a2a2a">
      <circle cx="1872" cy="1092" r="11"/>
      <circle cx="2171" cy="1084" r="11"/>
      <circle cx="2413" cy="1131" r="11"/>
    </g>
  </svg>

  <div class="dyn-value" style="left:1900px">0ms</div>
  <div class="dyn-value" style="left:2142px">12dBu</div>
  <div class="dyn-value" style="left:2385px">50dB/s</div>
  <div class="dyn-unit" style="left:1898px">MS</div>
  <div class="dyn-unit" style="left:2142px">THR</div>
  <div class="dyn-unit" style="left:2385px">REL</div>

</div>
</body>
</html>
```